Creative Business Card

Were looking for a new fresh and creative look to our Business card. Our company name is InkVale. Be creative, Were attaching our logo and our base colors, but your free to do anything. Name, title, Phone

Industry/Entity Type

Business

```html
<!DOCTYPE html>
<html lang="en">
<head>
<meta charset="utf-8">
<title>InkVale Business Card</title>
<link rel="stylesheet" href="https://fonts.googleapis.com/css2?family=Lato:ital,wght@0,300;0,400;0,700;0,900;1,700&display=swap">
<style>
  :root {
    --backdrop: #e4e5e7;
    --card: #ffffff;
    --brand-green: #7cc142;
    --brand-blue: #0f72ba;
    --text-blue: #1169b0;
    --on-blue: #ffffff;
    --shadow: rgba(0, 0, 0, 0.18);
  }
  * { margin: 0; padding: 0; box-sizing: border-box; }
  html, body {
    width: 1200px;
    height: 926px;
    overflow: hidden;
    background: var(--backdrop);
    font-family: "Lato", sans-serif;
  }
  .sheet {
    position: relative;
    width: 1200px;
    height: 926px;
  }
  .card {
    position: absolute;
    left: 280px;
    width: 640px;
    height: 366px;
    background: var(--card);
    overflow: hidden;
    box-shadow: 0 8px 24px var(--shadow);
  }
  .card--front { top: 64px; }
  .card--back { top: 496px; }
  .card__band {
    position: absolute;
    inset: 0;
    width: 100%;
    height: 100%;
  }
  .band-accent { fill: var(--brand-green); }
  .band-main { fill: var(--brand-blue); }

  .wordmark {
    position: absolute;
    left: 0;
    right: 0;
    text-align: center;
    color: var(--brand-green);
    font-weight: 900;
    letter-spacing: 1px;
    line-height: 1;
  }
  .card--front .wordmark { top: 34px; font-size: 64px; }
  .card--back .wordmark { top: 96px; font-size: 76px; }

  .contact {
    position: absolute;
    top: 118px;
    left: 0;
    right: 0;
    text-align: center;
    color: var(--text-blue);
  }
  .contact__name {
    font-size: 38px;
    font-weight: 300;
    line-height: 1.1;
  }
  .contact__surname { font-weight: 700; }
  .contact__line {
    font-size: 20px;
    font-weight: 400;
    line-height: 1.3;
    letter-spacing: 0.5px;
  }
  .contact__label {
    font-weight: 700;
    font-style: italic;
  }

  .address {
    position: absolute;
    top: 262px;
    left: 24px;
    width: 540px;
    text-align: center;
    color: var(--on-blue);
  }
  .address__title {
    font-size: 20px;
    font-weight: 700;
    letter-spacing: 0.5px;
  }
  .address__line {
    font-size: 17px;
    font-weight: 400;
    letter-spacing: 0.6px;
    margin-top: 4px;
  }

  .website {
    position: absolute;
    top: 268px;
    left: 120px;
    width: 240px;
    text-align: center;
    color: var(--on-blue);
    font-size: 14px;
    font-weight: 700;
    letter-spacing: 1.5px;
  }
</style>
</head>
<body>
<main class="sheet">

  <section class="card card--front" aria-label="Business card front">
    <svg class="card__band" viewBox="0 0 640 366" preserveAspectRatio="none" aria-hidden="true">
      <path class="band-accent" d="M0,234 Q230,188 640,325 L640,366 L0,366 Z"/>
      <path class="band-main" d="M0,243 Q240,200 640,340 L640,366 L0,366 Z"/>
    </svg>

    <div class="wordmark">InkVale</div>

    <div class="contact">
      <p class="contact__name">John <span class="contact__surname">Smith</span></p>
      <p class="contact__line"><span class="contact__label">phone:</span> 123-456-7890</p>
      <p class="contact__line"><span class="contact__label">email:</span> yourname@yourdomain.com</p>
    </div>

    <div class="address">
      <p class="address__title">ADDRESS</p>
      <p class="address__line">Street address goes here, Suite #303, Alt Bldg, NY 82365</p>
    </div>
  </section>

  <section class="card card--back" aria-label="Business card back">
    <svg class="card__band" viewBox="0 0 640 366" preserveAspectRatio="none" aria-hidden="true">
      <path class="band-accent" d="M0,232 Q280,212 640,342 L640,366 L0,366 Z"/>
      <path class="band-main" d="M0,240 Q260,224 640,358 L640,366 L0,366 Z"/>
    </svg>

    <div class="wordmark">InkVale</div>

    <p class="website">www.websitename.com</p>
  </section>

</main>
</body>
</html>
```